MH Marketing Piece

Marlin Hollow was created in 1984 as a shared aircraft ownership comprised of individual stockholders, interested in sharing the cost of aircraft ownership. Our strategy is simple, make owning and flying well maintained and upgraded aircraft more affordable through shared ownership.

When you own an aircraft individually, you have all the costs of a loan, hangar, insurance, subscriptions, annual inspection, and those unscheduled maintenance issues.

When you rent an aircraft from a local FBO, you get well used, dirty aircraft that everyone abuses with minimum hour requirements for weekend getaways that turn a 2 hour trip into a 9 hour hit on your wallet.

The solution? Shared aircraft ownership. Marlin Hollow has three aircraft based out of Corvel Regional (KPQJ). When you join a partnership, you split fixed costs between multiple individuals, AND get access to multiple well maintained and upgraded aircraft. When you fly, you pay the variable costs of your flight time only. Dividing the fixed expenses among multiple members makes flying much more affordable.

Benefits of shared aircraft ownership:

• Much cheaper than owning an aircraft individually
• Access to multiple aircraft
• Higher quality aircraft than your local FBO

• Hangared aircraft, flown by owners, not renters
• No overnight minimums
• On-line scheduling

www.marlinhollow-example.com

```html
<!DOCTYPE html>
<html lang="en">
<head>
<meta charset="utf-8">
<title>Marlin Hollow – Postcard</title>
<link rel="stylesheet" href="https://fonts.googleapis.com/css2?family=Cinzel:wght@400&family=Noto+Serif:wght@400&display=swap">
<style>
  :root {
    --page-bg: #eef1f4;
    --sky-top: #d3e8f6;
    --sky-mid: #eef6fc;
    --sky-low: #dcecf8;
    --navy: #1d3358;
    --ink: #1f2b3a;
    --blue-deep: #1d8ec8;
    --blue-bright: #36b2e7;
    --blue-steel: #2b7fb0;
    --blue-soft: #62c3e6;
    --photo-sky: #7fb2dc;
    --photo-ground: #6f6c68;
  }
  * { margin: 0; padding: 0; box-sizing: border-box; }
  html, body { width: 848px; height: 1200px; overflow: hidden; }
  body { background: var(--page-bg); position: relative; }

  .postcard {
    position: absolute;
    width: 612px;
    height: 462px;
    overflow: hidden;
    background:
      radial-gradient(ellipse 220px 90px at 30% 40%, rgba(255,255,255,.8), transparent 70%),
      radial-gradient(ellipse 260px 110px at 75% 70%, rgba(255,255,255,.7), transparent 70%),
      linear-gradient(180deg, var(--sky-top) 0%, var(--sky-mid) 45%, var(--sky-low) 100%);
    box-shadow: 0 4px 14px rgba(0,0,0,.25);
  }
  .postcard--front { left: 32px; top: 98px; }
  .postcard--back { left: 204px; top: 608px; }

  .facets { position: absolute; display: block; }

  /* Front */
  .brand {
    position: absolute; right: 34px; top: 16px;
    font-family: "Noto Serif", serif; font-weight: 400;
    font-size: 28px; color: var(--navy);
  }

  .benefits-banner {
    position: absolute; left: 6px; top: 82px; width: 448px; height: 36px;
    background: linear-gradient(180deg, #ffffff, #eef2f5);
    box-shadow: 0 2px 5px rgba(0,0,0,.35);
    font-family: "Cinzel", serif; font-weight: 400; font-size: 17px; color: var(--ink);
    line-height: 36px; padding-left: 36px;
  }
  .benefits-list {
    position: absolute; left: 26px; top: 134px; list-style: none;
    font-family: "Cinzel", serif; font-size: 14px; color: var(--ink);
    line-height: 17.5px;
  }
  .benefits-list li::before { content: "• "; }

  .aircraft-photo {
    position: absolute; width: 145px; height: 102px;
    background: linear-gradient(180deg, var(--photo-sky) 0%, #b9d3ea 50%, var(--photo-ground) 62%, #8a8782 100%);
  }
  .aircraft-photo--one { left: 164px; top: 305px; }
  .aircraft-photo--two { left: 306px; top: 253px; }
  .aircraft-photo--three { left: 448px; top: 201px; }

  .website {
    position: absolute; left: 44px; bottom: 24px;
    font-family: "Cinzel", serif; font-size: 15px; color: var(--ink);
  }

  /* Back */
  .about {
    position: absolute; left: 16px; top: 34px; width: 410px;
    font-family: "Noto Serif", serif; font-size: 13.5px; line-height: 17px;
    color: var(--ink); text-align: center;
  }
  .stamp-box {
    position: absolute; left: 438px; top: 14px; width: 140px; height: 138px;
    border: 2px dashed var(--ink);
  }
  .address-lines { position: absolute; left: 292px; top: 188px; width: 290px; }
  .address-lines span {
    display: block; border-top: 1px dashed #555; margin-bottom: 31px;
  }
</style>
</head>
<body>

<section class="postcard postcard--front">
  <svg class="facets" style="left:0;top:0" width="230" height="110" viewBox="0 0 230 110">
    <polygon points="0,0 120,0 0,70" fill="var(--blue-deep)"/>
    <polygon points="0,0 115,0 40,45" fill="var(--blue-steel)"/>
    <polygon points="0,20 60,60 0,100" fill="var(--blue-soft)"/>
    <polygon points="90,0 215,0 150,60" fill="var(--blue-bright)"/>
    <polygon points="150,0 215,0 150,60" fill="var(--blue-deep)"/>
  </svg>

  <h1 class="brand">Marlin Hollow</h1>

  <h2 class="benefits-banner">Benefits of shared aircraft ownership:</h2>
  <ul class="benefits-list">
    <li>Much cheaper than owning an aircraft individually</li>
    <li>Access to multiple aircraft</li>
    <li>Higher quality aircraft than your local FBO</li>
    <li>Hangared aircraft, flown by owners, not renters</li>
    <li>No overnight minimums</li>
    <li>On-line scheduling</li>
  </ul>

  <svg class="facets" style="left:0;top:0" width="612" height="462" viewBox="0 0 612 462">
    <path d="M0,330 Q300,260 612,90" fill="none" stroke="#a9cfe6" stroke-width="1"/>
  </svg>

  <div class="aircraft-photo aircraft-photo--one" role="img" aria-label="Photo of a white high-wing aircraft parked on the ramp"></div>
  <div class="aircraft-photo aircraft-photo--two" role="img" aria-label="Photo of a white low-wing aircraft on the ramp"></div>
  <div class="aircraft-photo aircraft-photo--three" role="img" aria-label="Photo of a low-wing aircraft with striped livery on the ramp"></div>

  <svg class="facets" style="right:0;bottom:0" width="230" height="120" viewBox="0 0 230 120">
    <polygon points="0,120 80,50 140,120" fill="var(--blue-deep)"/>
    <polygon points="60,120 80,50 140,120" fill="var(--blue-bright)"/>
    <polygon points="100,120 150,30 230,90 230,120" fill="var(--blue-steel)"/>
    <polygon points="150,30 230,0 230,90" fill="var(--blue-soft)"/>
  </svg>

  <p class="website">www.marlinhollow-example.com</p>
</section>

<section class="postcard postcard--back">
  <p class="about">Marlin Hollow was created in 1984 as a shared aircraft ownership comprised of individual stockholders, interested in sharing the cost of aircraft ownership. Our strategy is simple, make owning and flying well maintained and upgraded aircraft more affordable through shared ownership.</p>

  <div class="stamp-box" aria-label="Stamp area"></div>

  <div class="address-lines" aria-label="Address lines">
    <span></span><span></span><span></span><span></span>
  </div>

  <svg class="facets" style="left:0;top:180px" width="150" height="282" viewBox="0 0 150 282">
    <polygon points="0,0 80,70 0,130" fill="var(--blue-deep)"/>
    <polygon points="0,70 80,70 0,130" fill="var(--blue-bright)"/>
    <polygon points="0,130 100,205 0,250" fill="var(--blue-steel)"/>
    <polygon points="0,210 60,210 140,282 0,282" fill="var(--blue-soft)"/>
  </svg>

  <svg class="facets" style="right:0;bottom:0" width="230" height="110" viewBox="0 0 230 110">
    <polygon points="0,110 60,50 120,110" fill="var(--blue-deep)"/>
    <polygon points="60,50 110,110 60,110" fill="var(--blue-bright)"/>
    <polygon points="100,110 160,35 230,100 230,110" fill="var(--blue-steel)"/>
    <polygon points="160,35 230,10 230,100" fill="var(--blue-soft)"/>
  </svg>
</section>

</body>
</html>
```